Flyer-Design für meine Tätigkeit als freier Trauerredner
Zielgruppe
Für meine Tatigkeit als freier Trauerredner bei Beerdigungen möchte ich einen Flyer designen lassen, um diesen bei Bestattern aufzulegen sowie diese grundsätzlich als Informationsmaterial an interessierte Personen weitergeben zu können. Zielgruppe sind einerseits Personen, die sich lange im Vorfeld Gedanken über den Tod machen und den Wunsch äußern, im Rahmen einer persönlichen Gedenkfeier, unabhängig einer Konfessionszugehörigkeit und der Kirche verabschiedet zu werden. Auf der anderen Seite ist der Flyer ebenso für trauendernde Angehörige gedacht, die aufgrund eines unerwarteten Todesfalls sich mit dem Thema Beerdigung auseinadersetzen müssen und nach Alternativen zu einer krichlichen Beerdiugung suchen.
Aufgabenstellung
Eine Visitenkarte scheint mir im Format zu klein ... ein Flyer in einem größeren Format scheint mir geeigneter, Informationen zu vermitteln. Eine große Stärke von mir ist meine Emapthie. Der Flyer soll dies in der Bildsprache ausdrücken. Ebenso soll der Flyer durch die Bilder und die gewählte Sprahce Vertrauen aufbauen. Tod und Beerdigung sind für viele ein Tabuthemen ... der Flyer soll hier eine Brücke schlagen.
Wichtig wäre mir den Ablauf der Vorbereitung im Flyer aufzuskizzieren, um zu wissen, wie die Vorbereitung und Druchführung beispielhaft erfolgt.
Meine Kernaussage:
Freie Trauerreden, so einzigartig und besonders wie jeder Mensch selbst!
Als freier Trauerredner ist es mein Anspruch, den schweren Moment des Abschiednehmens so persönlich und würdevoll wie nur möglich zu gestalten!
Mein Ziel: Herzensverbindungen zwischen Menschen aufleben zu lassen und diese zu stärken. Herzensverbindungen leben und wirken weiter – unabhängig ob im Leben oder über den Tod hinaus!
Alle Informationen, die im Flyer aufgeführt werden sollen, sind dem beigefügten Word-Dokument zu entnehmen.
Wichtige Information finden Sie auf meiner Website www.tobiaskrämer.com
Wenn ein Statement oder Reszession benötigt wird und sich gut im Flyer macht, liefere ich diese gerne nach.

```html
<!DOCTYPE html>
<html lang="de">
<head>
<meta charset="utf-8">
<title>Freier Trauerredner Tobias Krämer</title>
<link rel="stylesheet" href="https://fonts.googleapis.com/css2?family=EB+Garamond:wght@400&family=Arimo:wght@400;700&display=swap">
<style>
  :root {
    --paper: #ffffff;
    --ink: #1a1a1a;
    --frame: #3a3a3a;
    --photo-warm: #d9cbb6;
    --photo-shadow: #8f857a;
    --photo-light: #f4efe7;
    --ornament: #f1f1f1;
  }
  html, body {
    margin: 0;
    padding: 0;
    width: 1200px;
    height: 1200px;
    overflow: hidden;
    background: var(--paper);
  }
  .flyer {
    position: relative;
    width: 1200px;
    height: 1200px;
    background: var(--paper);
    color: var(--ink);
    overflow: hidden;
  }
  .portrait {
    position: absolute;
    left: 0;
    top: 370px;
    width: 400px;
    height: 830px;
    background:
      radial-gradient(ellipse 55% 45% at 40% 70%, var(--photo-shadow) 0%, rgba(143,133,122,0.5) 45%, rgba(255,255,255,0) 75%),
      radial-gradient(ellipse 60% 40% at 30% 35%, var(--photo-warm) 0%, rgba(217,203,182,0.4) 50%, rgba(255,255,255,0) 80%),
      linear-gradient(90deg, var(--photo-light) 0%, rgba(255,255,255,0) 100%);
  }
  .frame {
    position: absolute;
    left: 0;
    top: 0;
    width: 1200px;
    height: 1200px;
    pointer-events: none;
  }
  .ornament {
    position: absolute;
    left: 864px;
    top: 89px;
    width: 283px;
    height: 187px;
    background: radial-gradient(ellipse at center, var(--ornament) 0%, rgba(241,241,241,0) 75%);
  }
  .motto {
    position: absolute;
    left: 411px;
    top: 178px;
    margin: 0;
    font-family: "EB Garamond", Georgia, serif;
    font-weight: 400;
    font-size: 38px;
    line-height: 48px;
  }
  .motto span { display: block; }
  .motto .indent { padding-left: 56px; }
  .info {
    position: absolute;
    left: 475px;
    top: 728px;
    width: 520px;
  }
  .info h2 {
    margin: 0 0 16px;
    font-family: "EB Garamond", Georgia, serif;
    font-weight: 400;
    font-size: 23px;
    line-height: 28px;
    letter-spacing: 0.2px;
  }
  .info p {
    margin: 0;
    font-family: "Arimo", Arial, sans-serif;
    font-size: 14.8px;
    line-height: 19.6px;
  }
  .info strong { font-weight: 700; }
  .about { margin-bottom: 28px; }
  .contact h2 { margin-bottom: 16px; }
</style>
</head>
<body>
<main class="flyer">
  <div class="portrait" role="img" aria-label="Porträtfoto des Trauerredners im hellen Gegenlicht, weißes Hemd und dunkle Weste"></div>

  <svg class="frame" viewBox="0 0 1200 1200" aria-hidden="true">
    <path d="M1043 45 H48 V1155 H1043 V268" fill="none" stroke="var(--frame)" stroke-width="1.2"/>
  </svg>

  <div class="ornament" role="img" aria-label="Feine Linienzeichnung eines fliegenden Vogels"></div>

  <h1 class="motto">
    <span>hier wäre ein</span>
    <span class="indent">schöner Spruch toll</span>
  </h1>

  <section class="info">
    <div class="about">
      <h2>ZU MEINER PERSON</h2>
      <p><strong>Freier Trauerredner Tobias Krämer</strong><br>
      Freier Trauerredner zu sein ist meine Berufung!<br>
      Mir ist es eine Freude, Menschen Halt und Kraft zu geben!<br>
      Das ist mein Ansporn – sowohl als freier Trauerredner<br>
      im Moment des Abschiednehmens, aber auch als Coach,<br>
      wenn es darum geht, wieder Halt und Kraft im Leben zu finden!</p>
    </div>
    <div class="contact">
      <h2>KONTAKT</h2>
      <p>Tobias Krämer<br>
      Birkenhof 12 I 94999 Talbach<br>
      Telefon/WhatsApp/Telegram: 0171 5550123<br>
      eMail: info@tobiaskrämer.com<br>
      Internet: www.tobiaskrämer.com</p>
    </div>
  </section>
</main>
</body>
</html>
```